New Innovative Counselling and psychotherapy Service needs Business Card design

Keep it simple and professional. On one side, just company name and logo (perhaps in all blue) and maybe a tag line.

On other side (all white) my name and Qualifications in centre

Industry/Entity Type

Health And Wellness

Contact Information for Business Card

Derek Hollis
Counsellor & Psychotherapist
BSc (Psychol.), BA, Dip. (Couns. & Psych.), PG.Cert (CBT), MGVrA, NWTF

I will also require Mobile no, Email and web site address of which I'll pass on to final designer.

Font styles to use
Sans Serif

Requirements
Must have
• My Logo Only and please use the colours in logo that is in it.
Should not have
• Any other images

```html
<!DOCTYPE html>
<html lang="en">
<head>
<meta charset="utf-8">
<title>Brightwell Lane – Business Card</title>
<link rel="stylesheet" href="https://fonts.googleapis.com/css2?family=Lato:wght@400;700;900&family=Raleway:wght@300;400&display=swap">
<style>
  :root {
    --backdrop: #e4e6e8;
    --brand-blue: #4fb3e5;
    --brand-green: #8dc63f;
    --qual-blue: #1f8fc4;
    --ink: #2b2b2b;
    --paper: #ffffff;
  }
  * { box-sizing: border-box; margin: 0; padding: 0; }
  html, body {
    width: 1200px; height: 926px; overflow: hidden;
    background: var(--backdrop);
  }
  .canvas {
    position: relative; width: 1200px; height: 926px;
    display: flex; flex-direction: column; align-items: center;
    justify-content: center; gap: 66px;
  }
  .card {
    position: relative; width: 700px; height: 400px;
    box-shadow: 0 6px 20px rgba(0,0,0,.16);
  }

  /* Front side */
  .card-front {
    background: var(--brand-blue);
    display: flex; align-items: center; justify-content: center; gap: 22px;
  }
  .brand-dot {
    width: 68px; height: 68px; border-radius: 50%; background: var(--paper);
  }
  .brand-name {
    font-family: "Raleway", sans-serif; font-weight: 300;
    font-size: 52px; color: var(--paper); letter-spacing: .5px;
  }

  /* Back side */
  .card-back { background: var(--paper); }
  .identity { position: absolute; left: 42px; top: 40px; }
  .person-name {
    font-family: "Lato", sans-serif; font-size: 30px; color: var(--ink);
    font-weight: 400; letter-spacing: .5px; line-height: 1;
  }
  .person-name .first { font-weight: 900; }
  .person-role {
    margin-top: 8px; font-family: "Lato", sans-serif; font-weight: 700;
    font-size: 14px; color: var(--brand-green); letter-spacing: .6px;
    text-transform: uppercase;
  }
  .person-quals {
    margin-top: 6px; font-family: "Lato", sans-serif; font-weight: 700;
    font-size: 10.5px; color: var(--qual-blue); letter-spacing: .3px;
    text-transform: uppercase;
  }
  .contact-list {
    position: absolute; left: 42px; bottom: 48px; list-style: none;
    font-family: "Lato", sans-serif; font-size: 22px; color: var(--ink);
  }
  .contact-list li { display: flex; align-items: center; gap: 12px; line-height: 1.45; }
  .contact-icon { width: 16px; height: 16px; fill: var(--qual-blue); flex: none; }
  .back-mark {
    position: absolute; right: 44px; bottom: 40px;
    display: flex; flex-direction: column; align-items: center; gap: 12px;
  }
  .back-mark .brand-dot { width: 150px; height: 150px; background: var(--brand-blue); }
  .back-mark .brand-name { font-size: 24px; color: var(--brand-blue); }
</style>
</head>
<body>
<main class="canvas">

  <section class="card card-front" aria-label="Card front">
    <span class="brand-dot" aria-hidden="true"></span>
    <span class="brand-name">Brightwell Lane</span>
  </section>

  <section class="card card-back" aria-label="Card back">
    <div class="identity">
      <h1 class="person-name"><span class="first">DEREK</span> HOLLIS</h1>
      <p class="person-role">Counsellor &amp; Psychotherapist</p>
      <p class="person-quals">BSc (Psychol.), BA, Dip (Couns. &amp; Psych.), PG.Cert (CBT), MGVrA, NWTF</p>
    </div>

    <ul class="contact-list">
      <li>
        <svg class="contact-icon" viewBox="0 0 16 16" aria-hidden="true"><path d="M3.5 1l2.5 3-1.5 2c1 2 2.5 3.5 4.5 4.5l2-1.5 3 2.5-1.5 2.5C7 14 2 9 1 2.5z"/></svg>
        <span>555-014-2387</span>
      </li>
      <li>
        <svg class="contact-icon" viewBox="0 0 16 16" aria-hidden="true"><path d="M6.5 9.5l3-3M7 4l1.5-1.5a3 3 0 0 1 4.2 4.2L11 8.5M9 12l-1.5 1.5a3 3 0 0 1-4.2-4.2L5 7.5" fill="none" stroke="#1f8fc4" stroke-width="1.8" stroke-linecap="round"/></svg>
        <span>www.derekhollis.net</span>
      </li>
      <li>
        <svg class="contact-icon" viewBox="0 0 16 16" aria-hidden="true"><path d="M1 3h14v10H1z"/><path d="M1.5 3.5L8 9l6.5-5.5" fill="none" stroke="#fff" stroke-width="1.4"/></svg>
        <span>hello@derekhollis.net</span>
      </li>
    </ul>

    <div class="back-mark">
      <span class="brand-dot" aria-hidden="true"></span>
      <span class="brand-name">Brightwell Lane</span>
    </div>
  </section>

</main>
</body>
</html>
```